Kelvara Learning Australia - Course Brochure Design

Kelvara Learning Australia is a Private Register Training Organisation that delivery accredited training courses to students. These courses are delivery via face to face training and distance education (e.g. elearning).

We are looking to get a template designed via adobe in design that we can use for each of our courses and list the information relevant for each one.

It will need to be around 3 - 4 pages long to be able to fit the information required into the brochure, i have attached some example of other providers course information sheets.

From the examples you'll be able to see that most of the information will remained the same until it gets to the course structure.

I would like it to be kept within our current theme, we are in the middle of upgrading our new website and look (www.kelvara.com.au/drupal).

I look forward to see what you all come back with.
Updates

Project Deadline Extended
Reason: Hi everyone, Thanks for submitting your design, I have extended the deadline due to not many designs have been submitted. I will be review and providing feedback on the designed submitted this week and will provide some more information based off the work and direction of the designs submitted. Thanks, Pedro.

Target Market(s)

our target market is business and individuals who would like to undergo training course. This brochure needs to display the require information.

Industry/Entity Type

Education

Requirements
Must have
• The brochure must have a front page with a design to list our company logo and information and the course title.

A call to action must be on every page, e.g. footer to enrol now call kelvra on 1800 392 058 or visit www.kelvara.com.au

Nice to have
• Some picture to fill the pages would add a nice look

```html
<!DOCTYPE html>
<html lang="en">
<head>
<meta charset="utf-8">
<title>Kelvara Learning Australia – Traineeship Brochure Cover</title>
<link href="https://fonts.googleapis.com/css2?family=Questrial&family=Open+Sans:wght@400;700&display=swap" rel="stylesheet">
<style>
  :root {
    --bg: #d9dde1;
    --navy: #24395a;
    --navy-deep: #123552;
    --blue: #2f6e9a;
    --blue-mid: #2a648c;
    --orange: #c8642a;
    --gold: #c9962c;
    --title-blue: #1f4e6e;
    --red: #8b1a14;
    --grey-swoosh: #6f7378;
    --white: #ffffff;
    --band-white: #f1f2f3;
    --text-dark: #2a2a2a;
    --rule: #a9b6c2;
    --placeholder: #c9ced3;
  }
  * { box-sizing: border-box; margin: 0; padding: 0; }
  html, body { width: 1200px; height: 900px; overflow: hidden; }
  body { background: var(--bg); position: relative; font-family: "Questrial", sans-serif; }

  .brochure-cover {
    position: absolute; left: 330px; top: 50px; width: 540px; height: 800px;
    background: var(--white); overflow: hidden;
    box-shadow: 0 4px 18px rgba(0,0,0,.18);
  }
  .colour-bar { position: absolute; top: 0; left: 0; width: 100%; height: 40px; display: flex; }
  .colour-bar span { height: 100%; }
  .colour-bar .seg-navy { width: 22%; background: var(--navy); }
  .colour-bar .seg-blue { width: 26%; background: var(--blue); }
  .colour-bar .seg-orange { width: 26%; background: var(--orange); }
  .colour-bar .seg-gold { width: 26%; background: var(--gold); }

  .section-band {
    position: absolute; top: 40px; left: 0; width: 100%; height: 50px;
    background: linear-gradient(var(--white), var(--band-white));
    display: flex; align-items: center; padding-left: 28px;
  }
  .section-title { font-size: 20px; color: var(--title-blue); letter-spacing: .5px; font-weight: 400; }

  .hero-panel {
    position: absolute; top: 90px; left: 0; width: 100%; height: 500px;
    background: radial-gradient(ellipse at 55% 40%, var(--blue-mid) 0%, var(--navy-deep) 75%);
  }
  .photo {
    position: absolute; border: 3px solid var(--white);
    box-shadow: 0 2px 6px rgba(0,0,0,.35);
  }
  .photo-meeting   { left: 43px;  top: 97px;  width: 115px; height: 78px;  background: linear-gradient(135deg,#8ea3b8,#e2e6ea); }
  .photo-classroom { left: 158px; top: 62px;  width: 230px; height: 150px; background: linear-gradient(135deg,#c9b9a8,#eee7df); }
  .photo-phone     { left: 388px; top: 110px; width: 112px; height: 112px; background: linear-gradient(135deg,#e9e6e2,#a8a29a); }
  .photo-headset   { left: 27px;  top: 177px; width: 147px; height: 113px; background: linear-gradient(135deg,#d8c0ae,#4c4e58); }
  .photo-laptop    { left: 172px; top: 217px; width: 113px; height: 133px; background: linear-gradient(135deg,#d6d1cb,#6c7f96); }
  .photo-study     { left: 285px; top: 217px; width: 175px; height: 190px; background: linear-gradient(135deg,#c9a07a,#b93a36 60%,#6a9a3c); }
  .photo-thumbs    { left: 460px; top: 217px; width: 68px;  height: 110px; background: linear-gradient(135deg,#f1f1f1,#2a2e38); }

  .wave { position: absolute; left: 0; top: 490px; width: 540px; height: 110px; }

  .course-title {
    position: absolute; top: 628px; left: 34px;
    font-size: 15.5px; color: var(--title-blue); letter-spacing: .4px; font-weight: 400;
  }
  .divider { position: absolute; top: 668px; left: 28px; right: 28px; border-top: 1px solid var(--rule); }

  .brand {
    position: absolute; top: 700px; left: 34px; display: flex; align-items: center; gap: 6px;
  }
  .brand-mark { width: 12px; height: 12px; border-radius: 50%; background: var(--red); }
  .brand-name { font-size: 20px; color: var(--red); font-weight: 400; }

  .contact {
    position: absolute; top: 678px; left: 152px;
    font-family: "Open Sans", sans-serif; font-style: normal;
    font-size: 8.6px; line-height: 11.5px; color: var(--text-dark);
  }
  .contact .org { font-weight: 700; color: var(--title-blue); font-size: 9.4px; }

  .accreditation-badge {
    position: absolute; top: 690px; left: 446px; width: 54px; height: 44px;
    background: var(--placeholder);
  }

  .footer-band {
    position: absolute; bottom: 0; left: 0; width: 100%; height: 48px;
    background: linear-gradient(90deg, var(--navy-deep), var(--blue) 55%, var(--navy-deep));
  }
</style>
</head>
<body>
  <main class="brochure-cover">
    <div class="colour-bar">
      <span class="seg-navy"></span><span class="seg-blue"></span><span class="seg-orange"></span><span class="seg-gold"></span>
    </div>

    <header class="section-band">
      <h1 class="section-title">| Traineeships</h1>
    </header>

    <section class="hero-panel">
      <div class="photo photo-meeting" role="img" aria-label="Photo of a team meeting around a table"></div>
      <div class="photo photo-classroom" role="img" aria-label="Photo of students studying together in a classroom"></div>
      <div class="photo photo-phone" role="img" aria-label="Photo of a businessman talking on a mobile phone"></div>
      <div class="photo photo-headset" role="img" aria-label="Photo of customer service staff wearing headsets"></div>
      <div class="photo photo-laptop" role="img" aria-label="Photo of students working on a laptop"></div>
      <div class="photo photo-study" role="img" aria-label="Photo of a student writing in a notebook outdoors"></div>
      <div class="photo photo-thumbs" role="img" aria-label="Photo of a businesswoman giving a thumbs up"></div>
    </section>

    <svg class="wave" viewBox="0 0 540 110" aria-hidden="true">
      <path d="M0,40 C100,70 200,88 300,80 C400,72 470,52 540,68 L540,110 L0,110 Z" fill="#ffffff"/>
      <path d="M130,77 C240,40 340,8 540,62" fill="none" stroke="#8b1a14" stroke-width="3"/>
      <path d="M12,62 C120,88 230,94 330,90 C420,86 500,86 540,96" fill="none" stroke="#6f7378" stroke-width="7"/>
    </svg>

    <h2 class="course-title">BSB30407 - Certificate III in Business Administration</h2>
    <div class="divider"></div>

    <div class="brand">
      <span class="brand-mark"></span>
      <span class="brand-name">Kelvara</span>
    </div>

    <address class="contact">
      <p class="org">Kelvara Learning Australia</p>
      <p>&gt;&gt; Address - 12/40 Marlow St, Hollis Park, Brisbane, QLD, 4170</p>
      <p>&gt;&gt; PO BOX 84, Dunmore QLD 4171</p>
      <p>&gt;&gt; Email - info@kelvara.com.au</p>
      <p>&gt;&gt; Phone - 1800 392 058</p>
      <p>&gt;&gt; Fax - 1800 275 614</p>
    </address>

    <div class="accreditation-badge" role="img" aria-label="Accreditation badge placeholder"></div>

    <footer class="footer-band"></footer>
  </main>
</body>
</html>
```